"Pause. Pivot. Prosper." Empowerment Book Cover

Hello, I need a hot, trendy, and contemporary book cover designed for my first book called "Pause. Pivot. Prosper. -- 365 Bold Confidence Notes for Anyone Seeking to Pause, Pivot, and Prosper Across Career & Personal Dreams."
This is my first book and I am really wanting to launch my brand with it... it would be awesome to match the inside/outside branding of the book. So we can either create the book cover to match the book guts, or update the book guts to match the cover.
Lastly, I just got a professional photoshoot done last week so we can use one of those images, or we can go with a different idea/style for the cover. The body of the book is attached. All questions welcomed, happy designing!
Target Market(s)
Gen Z, Millennials and Gen X.
Industry/Entity Type
Personal Development.
Requirements
Must have
- It must stand out and be different from other typical book covers.
Nice to have
- Success, Inspiration, Motivation, Mindset, Growth.
Should not have
- Clipart, stock art, stock look and feel.

```html
<!DOCTYPE html>
<html lang="en">
<head>
<meta charset="utf-8">
<title>Pause. Pivot. Prosper. — Book Cover</title>
<link rel="stylesheet" href="https://fonts.googleapis.com/css2?family=Poppins:wght@200;300;400;700&display=swap">
<style>
  :root {
    --stage: #dfe5e4;
    --cover-black: #050607;
    --backdrop-slate: #3f4b58;
    --backdrop-deep: #141b24;
    --suit-blue: #233489;
    --suit-shadow: #0f1640;
    --ink-white: #ffffff;
    --ink-soft: #e9ecef;
  }
  * { margin: 0; padding: 0; box-sizing: border-box; }
  html, body {
    width: 1200px;
    height: 675px;
    overflow: hidden;
    background: var(--stage);
    font-family: "Poppins", sans-serif;
  }
  .stage {
    width: 1200px;
    height: 675px;
    display: flex;
    align-items: center;
    justify-content: center;
  }
  .cover {
    position: relative;
    width: 450px;
    height: 675px;
    overflow: hidden;
    background: var(--cover-black);
    box-shadow: 0 18px 40px rgba(0, 0, 0, 0.25);
  }
  .cover__photo {
    position: absolute;
    inset: 0;
    background:
      linear-gradient(180deg, rgba(63, 75, 88, 0.55) 0%, rgba(20, 27, 36, 0.2) 45%, rgba(5, 6, 7, 0) 100%),
      linear-gradient(90deg, var(--cover-black) 0%, var(--cover-black) 22%, var(--backdrop-deep) 42%, var(--suit-shadow) 62%, var(--suit-blue) 82%, var(--suit-shadow) 100%);
  }
  .cover__title { font-weight: inherit; }
  .cover__title-line {
    position: absolute;
    left: 38px;
    color: var(--ink-white);
    line-height: 1;
    white-space: nowrap;
    letter-spacing: -0.5px;
  }
  .cover__title-line--pause   { top: 262px; font-size: 78px; font-weight: 200; }
  .cover__title-line--pivot   { top: 338px; font-size: 78px; font-weight: 400; }
  .cover__title-line--prosper { top: 415px; font-size: 76px; font-weight: 700; }
  .cover__subtitle {
    position: absolute;
    left: 39px;
    top: 521px;
    color: var(--ink-soft);
    font-size: 12.5px;
    font-weight: 300;
    line-height: 16px;
    text-transform: uppercase;
  }
  .cover__author {
    position: absolute;
    left: 0;
    right: 0;
    top: 600px;
    padding-left: 0;
    text-align: center;
    color: var(--ink-white);
    font-size: 21px;
    font-weight: 300;
    letter-spacing: 0.5px;
    text-transform: uppercase;
  }
</style>
</head>
<body>
  <main class="stage">
    <article class="cover">
      <div class="cover__photo" role="img" aria-label="Author portrait photograph in a blue suit against a dark studio backdrop"></div>
      <h1 class="cover__title">
        <span class="cover__title-line cover__title-line--pause">Pause.</span>
        <span class="cover__title-line cover__title-line--pivot">Pivot.</span>
        <span class="cover__title-line cover__title-line--prosper">Prosper.</span>
      </h1>
      <p class="cover__subtitle">365 Bold Confidence Notes for Anyone<br>Seeking to Pause, Pivot, and Prosper<br>Across Career &amp; Personal Dreams</p>
      <p class="cover__author">Samir Qadri</p>
    </article>
  </main>
</body>
</html>
```